K&M Digital Solutions- Linkwall Business Page

I need a linkwall business page design based on my company logo and colors. We are a Digital Marketing Company that helps business craft a detailed marketing campaigns to drive business to their company and help them reach their revenue goals and beyond. The design should be fun but professional and communicate growth.

Target Market(s)

no Target audience, should be geared toward general marketing for any business

Industry/Entity Type

Digital Marketing

Requirements
Must have
• Must have Company Name and Logo (K&M Digital Solutions) Email - colin@kmsolutionsqvx.com Phone Number (555)-417-3902
Nice to have
• Free Rain on Ideas

```html
<!DOCTYPE html>
<html lang="en">
<head>
<meta charset="utf-8">
<title>K&amp;M Digital Solutions – Linkwall Cover</title>
<link rel="stylesheet" href="https://fonts.googleapis.com/css2?family=Montserrat:wght@400;700&display=swap">
<style>
  :root {
    --green: #3a9a5b;
    --teal-dark: #1b4a46;
    --grey-text: #5f6163;
    --card-bg: #f1f1f1;
    --card-bg-light: #fafafa;
    --page-bg: #e4e3e3;
    --art-green: #9ccc65;
    --art-blue: #bcd6ee;
  }
  * { margin: 0; padding: 0; box-sizing: border-box; }
  html, body {
    width: 1200px; height: 755px; overflow: hidden;
    background: var(--page-bg);
    font-family: "Montserrat", sans-serif;
  }
  .cover {
    position: absolute; left: 0; top: 63px;
    width: 1200px; height: 628px;
    background: linear-gradient(125deg, var(--card-bg-light) 0%, var(--card-bg) 45%, var(--card-bg-light) 60%, var(--card-bg) 100%);
    overflow: hidden;
  }
  .brand {
    position: absolute; left: 71px; top: 92px;
    display: flex; align-items: center; gap: 12px;
  }
  .brand-dot {
    width: 26px; height: 26px; border-radius: 50%;
    background: var(--green);
  }
  .brand-name {
    font-weight: 700; font-size: 26px; color: var(--teal-dark);
    letter-spacing: 0.2px;
  }
  .headline-bar {
    position: absolute; left: 70px; top: 270px;
    width: 5px; height: 188px; background: var(--green);
  }
  .headline {
    position: absolute; left: 97px; top: 262px;
    font-size: 64px; line-height: 69px;
  }
  .headline span { display: block; }
  .headline .line-best { font-weight: 700; color: var(--green); }
  .headline .line-marketing { font-weight: 700; color: var(--teal-dark); }
  .headline .line-solutions { font-weight: 400; color: var(--grey-text); }
  .illustration {
    position: absolute; left: 690px; top: 88px;
    width: 390px; height: 440px;
    border-radius: 50% 50% 40% 45%;
    background: radial-gradient(circle at 45% 40%, var(--art-blue) 0%, var(--art-green) 55%, rgba(156,204,101,0) 75%);
    opacity: 0.75;
  }
  .contacts {
    position: absolute; left: 63px; top: 551px;
    display: flex; align-items: center;
    font-size: 25px; color: var(--teal-dark);
    white-space: nowrap;
  }
  .contact { display: flex; align-items: center; gap: 9px; }
  .contact svg { width: 24px; height: 24px; flex: none; }
  .contact .strong { font-weight: 700; color: var(--green); }
  .separator { color: var(--green); margin: 0 16px; font-weight: 700; }
</style>
</head>
<body>
  <main class="cover">
    <div class="brand">
      <div class="brand-dot"></div>
      <div class="brand-name">K&amp;M Digital Solutions</div>
    </div>

    <div class="headline-bar"></div>
    <h1 class="headline">
      <span class="line-best">Best Digital</span>
      <span class="line-marketing">Marketing</span>
      <span class="line-solutions">Solutions</span>
    </h1>

    <div class="illustration" role="img" aria-label="Illustration of digital marketing icons arranged in a question mark shape"></div>

    <div class="contacts">
      <div class="contact">
        <svg viewBox="0 0 24 24" aria-hidden="true">
          <circle cx="12" cy="12" r="12" fill="var(--teal-dark)"/>
          <path d="M8.3 6.5l1.8-.3 1.1 2.8-1.2 1c.6 1.4 1.6 2.4 3 3l1-1.2 2.8 1.1-.3 1.8c-.2.6-.8 1-1.5.9-3.8-.5-6.9-3.6-7.4-7.4-.1-.7.3-1.3.7-1.7z" fill="#fff"/>
        </svg>
        <span class="strong">(555)-417-3902</span>
      </div>
      <span class="separator">|</span>
      <div class="contact">
        <svg viewBox="0 0 24 24" aria-hidden="true">
          <circle cx="12" cy="12" r="12" fill="var(--teal-dark)"/>
          <rect x="6.5" y="8" width="11" height="8" rx="1" fill="#fff"/>
          <path d="M6.8 8.4l5.2 4 5.2-4" fill="none" stroke="var(--teal-dark)" stroke-width="1.2"/>
        </svg>
        <span>colin@<span class="strong">kmsolutionsqvx</span>.com</span>
      </div>
      <span class="separator">|</span>
      <div class="contact">
        <svg viewBox="0 0 24 24" aria-hidden="true">
          <circle cx="12" cy="12" r="12" fill="var(--teal-dark)"/>
          <g fill="none" stroke="#fff" stroke-width="1.2">
            <circle cx="12" cy="12" r="5.8"/>
            <ellipse cx="12" cy="12" rx="2.5" ry="5.8"/>
            <path d="M6.2 12h11.6M7 9h10M7 15h10"/>
          </g>
        </svg>
        <span>www.<span class="strong">kmsolutionsqvx</span>.com</span>
      </div>
    </div>
  </main>
</body>
</html>
```